Executive Performance Review mapped on J-curve

I need to turn an executive company performance review into a visual infographic. The list of accomplishments is grouped into four calendar quarters. Each quarter needs a subtle representation of the season. The four quarters and associated list of accomplishments need to be mapped to a J-curve. - Spreadsheet with accomplishments attached (Throughput)- Sample image of a J-curve. You can google J-curve to see more images.- The title should be "Danela Morsky Year in Review"

Target Market(s)

Board of Directors

Requirements
Nice to have
• This will be presented to a company founder that is an artist and customer experience expert. He is very visual so a nice visual representation of the data will be impactful. He also uses the phrase that you have to live with or work with someone for four seasons before you really know them. This is why I have the seasons mapped to the quarters. The Fall season motif should be gloomy and stormy.

```html
<!DOCTYPE html>
<html lang="en">
<head>
<meta charset="utf-8">
<title>Danela Morsky Year in Review</title>
<link href="https://fonts.googleapis.com/css2?family=Roboto+Condensed:wght@400;500;700&display=swap" rel="stylesheet">
<style>
:root{
  --summer:#e8473b;
  --fall:#9db51f;
  --winter:#f7923a;
  --spring:#2aabab;
  --curve:#2e2e2e;
  --card-body:#f2f2f2;
  --card-edge:#d6d6d6;
  --ink:#3d3d3d;
  --rule:#c9c9c9;
}
*{margin:0;padding:0;box-sizing:border-box}
html,body{width:1200px;height:754px;overflow:hidden;background:#fff}
body{position:relative;font-family:"Roboto Condensed",Arial Narrow,sans-serif;color:var(--ink)}
.connectors{position:absolute;left:0;top:0}
.card{position:absolute;background:var(--card-body);border:1px solid var(--card-edge);border-radius:7px;box-shadow:0 1px 2px rgba(0,0,0,.18)}
.card h3{height:18px;line-height:18px;text-align:center;color:#fff;font-weight:500;font-size:11px;border-radius:6px 6px 0 0}
.card ul{list-style:none;padding:4px 4px 0 7px}
.card li{font-size:8.1px;line-height:11.6px;padding-left:5px;text-indent:-5px;letter-spacing:-.1px}
.card li::before{content:"• "}
.card.tab-r::after,.card.tab-l::after{content:"";position:absolute;top:50%;width:8px;height:18px;margin-top:-9px;background:#dcdcdc}
.card.tab-r::after{right:-9px;border-radius:0 9px 9px 0}
.card.tab-l::after{left:-9px;border-radius:9px 0 0 9px}
.summer h3{background:var(--summer)}
.fall h3{background:var(--fall)}
.winter h3{background:var(--winter)}
.spring h3{background:var(--spring)}
.season{position:absolute;color:#fff;text-align:center;border-radius:7px;border:2px solid rgba(255,255,255,.0);box-shadow:0 1px 3px rgba(0,0,0,.25);padding-top:2px}
.season .name{display:block;font-size:22px;line-height:22px;font-weight:500}
.season .quarter{display:block;font-size:17px;line-height:18px}
.season .theme{display:block;font-size:12px;line-height:15px;letter-spacing:1px;font-weight:500}
.season.summer{background:var(--summer)}
.season.fall{background:var(--fall)}
.season.winter{background:var(--winter)}
.season.spring{background:var(--spring)}
</style>
</head>
<body>
<svg class="connectors" width="1200" height="754" viewBox="0 0 1200 754">
  <g stroke="var(--rule)" stroke-width="1.2" fill="none">
    <line x1="408" y1="90" x2="408" y2="331"/>
    <line x1="385" y1="90" x2="408" y2="90"/>
    <line x1="219" y1="145" x2="408" y2="145"/>
    <line x1="385" y1="210" x2="408" y2="210"/>
    <line x1="219" y1="281" x2="408" y2="281"/>
    <line x1="385" y1="331" x2="408" y2="331"/>
    <line x1="410" y1="522" x2="410" y2="691"/>
    <line x1="372" y1="522" x2="410" y2="522"/>
    <line x1="220" y1="578" x2="410" y2="578"/>
    <line x1="372" y1="635" x2="410" y2="635"/>
    <line x1="220" y1="691" x2="410" y2="691"/>
    <line x1="802" y1="375" x2="802" y2="618"/>
    <line x1="802" y1="375" x2="826" y2="375"/>
    <line x1="802" y1="436" x2="992" y2="436"/>
    <line x1="802" y1="496" x2="826" y2="496"/>
    <line x1="802" y1="557" x2="992" y2="557"/>
    <line x1="802" y1="618" x2="826" y2="618"/>
    <line x1="803" y1="83" x2="803" y2="267"/>
    <line x1="803" y1="83" x2="827" y2="83"/>
    <line x1="803" y1="145" x2="993" y2="145"/>
    <line x1="803" y1="206" x2="827" y2="206"/>
    <line x1="803" y1="267" x2="993" y2="267"/>
  </g>
  <g fill="var(--summer)"><circle cx="408" cy="90" r="4"/><circle cx="408" cy="145" r="4"/><circle cx="408" cy="210" r="4"/><circle cx="408" cy="281" r="4"/><circle cx="408" cy="331" r="4"/></g>
  <g fill="var(--fall)"><circle cx="410" cy="522" r="4"/><circle cx="410" cy="578" r="4"/><circle cx="410" cy="635" r="4"/><circle cx="410" cy="691" r="4"/></g>
  <g fill="var(--winter)"><circle cx="802" cy="375" r="4"/><circle cx="802" cy="436" r="4"/><circle cx="802" cy="496" r="4"/><circle cx="802" cy="557" r="4"/><circle cx="802" cy="618" r="4"/></g>
  <g fill="var(--spring)"><circle cx="803" cy="83" r="4"/><circle cx="803" cy="145" r="4"/><circle cx="803" cy="206" r="4"/><circle cx="803" cy="267" r="4"/></g>

  <path d="M409,436 C418,478 445,504 496,510 C575,514 615,455 657,378 L765,190 L781,166" fill="none" stroke="var(--curve)" stroke-width="13" stroke-linecap="round"/>
  <path d="M409,436 L405,428" stroke="var(--curve)" stroke-width="3"/>

  <g class="icon-sun">
    <circle cx="421" cy="462" r="20" fill="var(--summer)" stroke="#fff" stroke-width="1.5"/>
    <circle cx="421" cy="462" r="6" fill="none" stroke="#fff" stroke-width="1.6"/>
    <g stroke="#fff" stroke-width="1.6" stroke-linecap="round">
      <line x1="421" y1="449" x2="421" y2="452"/><line x1="421" y1="472" x2="421" y2="475"/>
      <line x1="408" y1="462" x2="411" y2="462"/><line x1="431" y1="462" x2="434" y2="462"/>
      <line x1="412" y1="453" x2="414" y2="455"/><line x1="428" y1="469" x2="430" y2="471"/>
      <line x1="430" y1="453" x2="428" y2="455"/><line x1="414" y1="469" x2="412" y2="471"/>
    </g>
  </g>
  <g class="icon-leaf-fall">
    <circle cx="496" cy="507" r="20" fill="var(--fall)" stroke="#fff" stroke-width="1.5"/>
    <path d="M496,494 L499,501 L505,499 L503,506 L508,508 L501,512 L502,516 L496,514 L490,516 L491,512 L484,508 L489,506 L487,499 L493,501 Z" fill="#fff"/>
    <line x1="496" y1="513" x2="496" y2="521" stroke="#fff" stroke-width="1.3"/>
  </g>
  <g class="icon-snow">
    <circle cx="657" cy="378" r="20" fill="var(--winter)" stroke="#fff" stroke-width="1.5"/>
    <g stroke="#fff" stroke-width="1.5" stroke-linecap="round">
      <line x1="657" y1="366" x2="657" y2="390"/>
      <line x1="646.6" y1="372" x2="667.4" y2="384"/>
      <line x1="646.6" y1="384" x2="667.4" y2="372"/>
      <polyline points="654,368 657,371 660,368" fill="none"/>
      <polyline points="654,388 657,385 660,388" fill="none"/>
    </g>
  </g>
  <g class="icon-leaf-spring">
    <circle cx="769" cy="196" r="20" fill="var(--spring)" stroke="#fff" stroke-width="1.5"/>
    <path d="M769,183 C778,190 778,202 769,209 C760,202 760,190 769,183 Z" fill="none" stroke="#fff" stroke-width="1.5"/>
    <g stroke="#fff" stroke-width="1.2" fill="none">
      <line x1="769" y1="186" x2="769" y2="212"/>
      <polyline points="764,192 769,196 774,192"/>
      <polyline points="764,198 769,202 774,198"/>
    </g>
  </g>
</svg>

<!-- Summer -->
<section class="card summer tab-r" style="left:231px;top:50px;width:154px;height:75px">
  <h3>Transition</h3>
  <ul><li>RO Transition from Rob &amp; Lina</li><li>Start CR Office Initiative</li><li>Tactical Ops transition from Rob</li><li>Formalize Exec Team</li></ul>
</section>
<section class="card summer tab-r" style="left:65px;top:105px;width:154px;height:86px">
  <h3>Biz Architecture</h3>
  <ul><li>Independent Financial Audit</li><li>Organizational Audit - Structure</li><li>Organizational Audit - People</li><li>XF Framework - ESU</li><li>Defined Utilization, Realization, Availability</li></ul>
</section>
<section class="card summer tab-r" style="left:231px;top:164px;width:154px;height:90px">
  <h3>Strategy</h3>
  <ul><li>Effective Strategy Meeting</li><li>Strategic Themes 2018 - 2020: Stablize, Accelerate, Surge</li><li>Business Drivers: Drive Revenue, Improve Veritas Experience, Increase Brand Awareness</li></ul>
</section>
<section class="card summer tab-r" style="left:65px;top:244px;width:154px;height:75px">
  <h3>Sales</h3>
  <ul><li>Harlow Account Transition</li><li>Ferro Account Transition</li><li>2 year Managed Services Engagement Model</li></ul>
</section>
<section class="card summer tab-r" style="left:231px;top:309px;width:154px;height:44px">
  <h3>Revenue / EBITA</h3>
  <ul><li>TBD</li></ul>
</section>
<div class="season summer" style="left:359px;top:370px;width:95px;height:59px">
  <span class="name">Summer</span><span class="quarter">Q3 2018</span><span class="theme">Assessment</span>
</div>

<!-- Fall -->
<section class="card fall tab-r" style="left:74px;top:506px;width:146px;height:145px">
  <h3>Biz Architecture</h3>
  <ul><li>XF Framework - Functional Meetings &amp; Scrum of Scrums</li><li>Structured Reorg</li><li>Implemented Reorg</li><li>Quarterly Org Iteration cadence</li><li>Defined Key Hire Plan</li><li>CR Office Operational</li><li>Time Accountability</li><li>Tools ReConfig</li><li>Org Structure v1</li></ul>
</section>
<section class="card fall tab-r" style="left:247px;top:501px;width:125px;height:42px">
  <h3>Strategy</h3>
  <ul><li>Internal QBR Accountability</li></ul>
</section>
<section class="card fall tab-r" style="left:247px;top:611px;width:125px;height:47px">
  <h3>Sales</h3>
  <ul><li>Kestrel QBR</li><li>Harlow QBR</li></ul>
</section>
<section class="card fall tab-r" style="left:74px;top:672px;width:146px;height:41px">
  <h3>Revenue / EBITA</h3>
  <ul><li>TBD</li></ul>
</section>
<div class="season fall" style="left:453px;top:533px;width:91px;height:59px">
  <span class="name">Fall</span><span class="quarter">Q4 2018</span><span class="theme">Stablize</span>
</div>

<!-- Winter -->
<section class="card winter tab-l" style="left:826px;top:338px;width:154px;height:74px">
  <h3>Biz Architecture</h3>
  <ul><li>XF Framework - Progress Demos</li><li>Org Structure - COE's</li><li>Stablize Accounting &amp; Finance</li><li>Exec Hiring Process</li></ul>
</section>
<section class="card winter" style="left:992px;top:407px;width:154px;height:59px">
  <h3>Key Hires</h3>
  <ul><li>Controller</li><li>Director CX</li></ul>
</section>
<section class="card winter tab-l" style="left:826px;top:469px;width:154px;height:56px">
  <h3>Strategy</h3>
  <ul><li>Founders removed from front line activity</li><li>Veritas QBR - Goal Setting &amp; Tracking</li></ul>
</section>
<section class="card winter" style="left:992px;top:534px;width:154px;height:48px">
  <h3>Sales</h3>
  <ul><li>Ferro QBR</li><li>Harlow QBR</li></ul>
</section>
<section class="card winter tab-l" style="left:826px;top:594px;width:154px;height:48px">
  <h3>Revenue / EBITA</h3>
  <ul><li>TBD</li></ul>
</section>
<div class="season winter" style="left:689px;top:357px;width:94px;height:59px">
  <span class="name">Winter</span><span class="quarter">Q1 2018</span><span class="theme">Stratactical</span>
</div>

<!-- Spring -->
<section class="card spring tab-l" style="left:827px;top:46px;width:154px;height:74px">
  <h3>Biz Architecture</h3>
  <ul><li>Tiered Pricing Pre-Paid Engagement Model</li><li>XF Framework - Ideation Board</li><li>Consulting Levels &amp; Salary Bands</li><li>Roles &amp; Responsibilities</li></ul>
</section>
<section class="card spring" style="left:993px;top:97px;width:154px;height:95px">
  <h3>Key Hires</h3>
  <ul><li>Interim HR</li><li>Provisional Client Partner</li><li>Acting Director 1</li><li>Acting Director 2</li><li>Client Partner 1</li><li>Sales Exec 1</li></ul>
</section>
<section class="card spring tab-l" style="left:827px;top:170px;width:154px;height:71px">
  <h3>Sales</h3>
  <ul><li>Opened BrightPane Door</li><li>Flipped focus from operationaly run company to sales/marketing driven org</li><li>Northway Direct</li></ul>
</section>
<section class="card spring" style="left:993px;top:246px;width:154px;height:42px">
  <h3>Revenue / EBITA</h3>
  <ul><li>TBD</li></ul>
</section>
<div class="season spring" style="left:656px;top:156px;width:85px;height:59px">
  <span class="name">Spring</span><span class="quarter">Q2 2018</span><span class="theme">Strategic</span>
</div>
</body>
</html>
```